Quorival Corporate Vision Mission Statement Infographic

We need an info graphic which summarizes and visually explains the companies Ambition Statement, Strategic Priorities, Principles and Brand Actions and how they relate to each other

```html
<!DOCTYPE html>
<html lang="en">
<head>
<meta charset="utf-8">
<title>Quorival Corporate Vision Infographic</title>
<link rel="stylesheet" href="https://fonts.googleapis.com/css2?family=Montserrat:wght@400;500;600;700&display=swap">
<style>
:root{
  --blue:#4a6cc3;
  --navy:#2f4a9a;
  --orange:#f37021;
  --peach:#fde1d3;
  --lavender:#dde0f1;
  --card:#e9eaf5;
  --ink:#2b2b2b;
  --white:#ffffff;
}
*{margin:0;padding:0;box-sizing:border-box}
html,body{width:1200px;height:4478px;overflow:hidden;background:var(--white)}
body{position:relative;font-family:"Montserrat",sans-serif;color:var(--ink)}
.abs{position:absolute}
.brand{display:flex;align-items:center;justify-content:center;left:0;width:1200px}
.brand-name{font-weight:700;font-size:62px;color:var(--navy);letter-spacing:-1px;line-height:1}
.photo{border-radius:26px}
.hero-side-left{left:0;top:150px;width:149px;height:530px;border-radius:0 26px 26px 0;background:linear-gradient(180deg,#f1d6d7 0%,#e9b69a 45%,#8d8150 75%,#5a6a36 100%)}
.hero-side-right{left:1054px;top:150px;width:146px;height:530px;border-radius:26px 0 0 26px;background:linear-gradient(180deg,#f3dcd8 0%,#e2b48f 45%,#8c8a4f 75%,#566a39 100%)}
.hero-main{left:218px;top:150px;width:767px;height:530px;background:linear-gradient(180deg,#f3e4e6 0%,#f2d2c8 40%,#c3a270 68%,#6e7346 100%)}
.hero-title{left:280px;top:172px;font-size:50px;line-height:58px;font-weight:700;color:var(--blue)}
.card{top:734px;width:345px;height:317px;background:var(--card);border-radius:14px}
.card-art{position:absolute;left:72px;top:28px;width:200px;height:190px;border-radius:14px}
.card-label{position:absolute;left:0;width:100%;bottom:18px;text-align:center;font-size:31px;font-weight:600;color:var(--navy);line-height:38px}
.band{left:57px;width:1098px;height:92px;background:var(--blue);border-radius:6px;color:var(--white);font-size:34px;font-weight:600;display:flex;align-items:center;justify-content:center;letter-spacing:.5px}
.ambition-text{left:439px;top:1272px;font-size:30px;line-height:44px;color:var(--ink);white-space:nowrap}
.priority-photo{top:1719px;width:334px;height:448px}
.priority-label{top:2186px;width:360px;text-align:center;font-size:29px;line-height:40px;color:var(--ink);white-space:nowrap}
.num{display:inline-block;width:30px;height:30px;border-radius:50%;background:var(--blue);color:var(--white);font-size:18px;line-height:30px;text-align:center;font-weight:600;vertical-align:3px;margin-right:10px}
.col-head{top:2454px;height:72px;color:var(--white);font-size:31px;font-weight:600;display:flex;align-items:center;justify-content:center}
.col-principle{left:412px;top:2526px;width:361px;height:1802px;background:var(--peach)}
.col-action{left:773px;top:2526px;width:364px;height:1802px;background:var(--lavender)}
.row-photo{left:72px;width:310px;height:344px}
.cell{width:361px;height:344px;display:flex;flex-direction:column;align-items:center}
.cell svg{margin-top:104px;width:116px;height:116px}
.cell-text{margin-top:44px;font-size:30px;color:var(--ink);white-space:nowrap}
.principle-text{text-transform:uppercase}
.icon-o{fill:var(--orange)}
.icon-b{fill:var(--navy)}
</style>
</head>
<body>

<div class="abs brand" style="top:30px;height:105px"><span class="brand-name">Quorival</span></div>

<div class="abs hero-side-left" role="img" aria-label="Sunset over rolling hills"></div>
<div class="abs photo hero-main" role="img" aria-label="Traveller with arms raised on a rocky overlook at sunset"></div>
<div class="abs hero-side-right" role="img" aria-label="Evening valley landscape"></div>
<div class="abs hero-title">Dream.<br>Explore.<br>Travel On.</div>

<div class="abs card" style="left:57px">
  <div class="card-art" role="img" aria-label="Hand pointing at an orange target" style="background:radial-gradient(circle at 55% 45%,#f37021 0 30%,#f8b48a 31% 55%,#e9eaf5 56%)"></div>
  <div class="card-label">Ambition</div>
</div>
<div class="abs card" style="left:436px">
  <div class="card-art" role="img" aria-label="Two hands in a handshake" style="background:linear-gradient(90deg,#e9eaf5 0%,#f5c6a3 35%,#f5c6a3 65%,#e9eaf5 100%)"></div>
  <div class="card-label">Strategic Priorities</div>
</div>
<div class="abs card" style="left:812px">
  <div class="card-art" role="img" aria-label="Two interlocking puzzle pieces labelled principles and brand actions" style="background:linear-gradient(90deg,#f37021 0 50%,#4a6cc3 50% 100%);height:150px;top:40px"></div>
  <div class="card-label">Principles and<br>Brand Actions</div>
</div>

<div class="abs band" style="top:1104px">AMBITION</div>
<div class="abs photo" role="img" aria-label="Hands holding a small globe" style="left:72px;top:1224px;width:349px;height:322px;border-radius:10px;background:radial-gradient(circle at 50% 45%,#d9d1c4 0 18%,#7a5a45 40%,#3a2a22 100%)"></div>
<p class="abs ambition-text">Our dream is to be a globally recognized<br>travel protection provider with heart—strive<br>to be the best in the eyes of our customers<br>as they travel and explore the world safely.</p>

<div class="abs band" style="top:1594px">STRATEGIC PRIORITIES</div>
<div class="abs photo priority-photo" role="img" aria-label="Smiling couple on a boat at sea" style="left:72px;background:linear-gradient(160deg,#2f4e63 0%,#5b7d91 45%,#d9dde0 75%,#8aa2b2 100%)"></div>
<div class="abs photo priority-photo" role="img" aria-label="Person relaxing in a hammock with a tablet" style="left:439px;background:linear-gradient(180deg,#b8d58c 0%,#7fa957 45%,#e0703e 75%,#c94b2c 100%)"></div>
<div class="abs photo priority-photo" role="img" aria-label="Group of friends embracing at a mountain viewpoint" style="left:797px;background:linear-gradient(180deg,#a9c3e3 0%,#7f97b4 40%,#5f6d4a 70%,#8f7b5e 100%)"></div>
<div class="abs priority-label" style="left:60px"><span class="num">1</span>Transform The<br>Customer Experience</div>
<div class="abs priority-label" style="left:424px"><span class="num">2</span>Simplify<br>The Complex</div>
<div class="abs priority-label" style="left:784px"><span class="num">3</span>Build Successful<br>Partnerships</div>

<div class="abs band" style="top:2334px;left:54px;width:1095px">PRINICPLES AND BRAND ACTIONS</div>

<div class="abs col-head" style="left:412px;width:358px;background:var(--orange)">PRINCIPLE</div>
<div class="abs col-head" style="left:773px;width:364px;background:var(--blue)">BRAND ACTION</div>
<div class="abs col-principle"></div>
<div class="abs col-action"></div>

<div class="abs photo row-photo" role="img" aria-label="Surfer with a board on a coastal cliff" style="top:2528px;background:linear-gradient(180deg,#c9d6e0 0%,#8ea3a8 40%,#6c7a63 70%,#c7b59a 100%)"></div>
<div class="abs photo row-photo" role="img" aria-label="Two hikers with backpacks on a forest trail" style="top:2892px;background:linear-gradient(180deg,#5e7a3a 0%,#8aa45a 40%,#3b5a8c 75%,#6f5a44 100%)"></div>
<div class="abs photo row-photo" role="img" aria-label="Woman in a knit hat talking on a phone in a city" style="top:3256px;background:linear-gradient(180deg,#8a6f66 0%,#b38c7d 40%,#7c4b8c 70%,#5b5a62 100%)"></div>
<div class="abs photo row-photo" role="img" aria-label="Traveller sitting on a boat bow facing a bright sea" style="top:3620px;background:linear-gradient(180deg,#f6ecc8 0%,#d7c89a 40%,#6c7b7f 70%,#3a4a52 100%)"></div>
<div class="abs photo row-photo" role="img" aria-label="Mountaineer beneath prayer flags on a snowy summit" style="top:3984px;background:linear-gradient(180deg,#3d68b4 0%,#7ea0d4 40%,#dfe4ea 70%,#9aa3ad 100%)"></div>

<div class="abs cell" style="left:412px;top:2528px">
  <svg viewBox="0 0 100 100"><circle class="icon-o" cx="50" cy="38" r="32"/><circle cx="50" cy="38" r="22" fill="var(--peach)"/><polygon class="icon-o" points="50,22 55,33 67,34 58,42 61,54 50,48 39,54 42,42 33,34 45,33"/><polygon class="icon-o" points="30,62 22,96 36,88 44,98 48,70"/><polygon class="icon-o" points="70,62 78,96 64,88 56,98 52,70"/></svg>
  <div class="cell-text principle-text">Excellence</div>
</div>
<div class="abs cell" style="left:412px;top:2892px">
  <svg viewBox="0 0 100 100"><path class="icon-o" d="M4 40 L24 28 L44 38 L58 30 L76 28 L96 40 L86 62 L70 76 Q64 82 58 76 L50 82 Q44 86 40 80 L32 84 Q26 86 24 78 L14 64 Z"/><path d="M44 38 L34 50 Q40 56 48 48 L58 44 L76 62" fill="none" stroke="var(--peach)" stroke-width="4"/></svg>
  <div class="cell-text principle-text">Commitment</div>
</div>
<div class="abs cell" style="left:412px;top:3256px">
  <svg viewBox="0 0 100 100"><path d="M50 46 C30 30 30 8 44 8 C48 8 50 12 50 14 C50 12 52 8 56 8 C70 8 70 30 50 46 Z" fill="none" stroke="var(--orange)" stroke-width="5"/><path d="M6 62 L28 56 Q40 54 52 62 L64 64 Q70 68 64 72 L44 72 M60 72 L84 60 Q94 58 90 68 L66 88 Q58 94 48 92 L20 88 L6 90" fill="none" stroke="var(--orange)" stroke-width="5" stroke-linejoin="round"/></svg>
  <div class="cell-text principle-text">Compassion</div>
</div>
<div class="abs cell" style="left:412px;top:3620px">
  <svg viewBox="0 0 100 100"><path class="icon-o" d="M50 4 L86 16 L86 46 Q86 78 50 96 Q14 78 14 46 L14 16 Z"/><path d="M32 50 L45 63 L70 36" fill="none" stroke="var(--peach)" stroke-width="8" stroke-linecap="round" stroke-linejoin="round"/></svg>
  <div class="cell-text principle-text">Integrity</div>
</div>
<div class="abs cell" style="left:412px;top:3984px">
  <svg viewBox="0 0 100 100"><circle class="icon-o" cx="50" cy="14" r="11"/><path class="icon-o" d="M8 30 L92 30 L92 40 L62 40 L62 96 L52 96 L52 68 L48 68 L48 96 L38 96 L38 40 L8 40 Z"/></svg>
  <div class="cell-text principle-text">Independence</div>
</div>

<div class="abs cell" style="left:773px;top:2528px;width:364px">
  <svg viewBox="0 0 100 100"><path class="icon-b" d="M4 96 L38 40 L50 56 L60 44 L96 96 Z"/><rect class="icon-b" x="60" y="6" width="4" height="40"/><polygon class="icon-b" points="64,6 86,13 64,20"/><circle class="icon-b" cx="40" cy="30" r="6"/></svg>
  <div class="cell-text">Embrace challenge</div>
</div>
<div class="abs cell" style="left:773px;top:2892px;width:364px">
  <svg viewBox="0 0 100 100"><polygon class="icon-b" points="34,6 46,6 42,96 10,96"/><polygon class="icon-b" points="54,6 66,6 90,96 58,96"/><rect class="icon-b" x="48" y="14" width="4" height="14"/><rect class="icon-b" x="48" y="40" width="4" height="16"/><rect class="icon-b" x="47" y="68" width="6" height="20"/></svg>
  <div class="cell-text">Go the extra mile</div>
</div>
<div class="abs cell" style="left:773px;top:3256px;width:364px">
  <svg viewBox="0 0 100 100"><circle class="icon-b" cx="32" cy="14" r="11"/><path class="icon-b" d="M18 30 L46 30 L46 96 L36 96 L36 66 L28 66 L28 96 L18 96 Z"/><path class="icon-b" d="M60 44 L74 44 L74 56 L86 56 L86 70 L74 70 L74 84 L60 84 L60 70 L50 70 L50 56 L60 56 Z"/></svg>
  <div class="cell-text">Put people first</div>
</div>
<div class="abs cell" style="left:773px;top:3620px;width:364px">
  <svg viewBox="0 0 100 100"><rect class="icon-b" x="6" y="42" width="20" height="52" rx="3"/><path class="icon-b" d="M32 44 L50 8 Q62 6 60 24 L56 38 L88 38 Q98 40 94 52 L86 86 Q82 94 72 94 L32 94 Z"/></svg>
  <div class="cell-text">Do the right thing</div>
</div>
<div class="abs cell" style="left:773px;top:3984px;width:364px">
  <svg viewBox="0 0 100 100"><circle class="icon-b" cx="50" cy="12" r="10"/><path class="icon-b" d="M38 26 L62 26 L62 62 L56 62 L56 96 L44 96 L44 62 L38 62 Z"/><circle class="icon-b" cx="22" cy="22" r="8"/><path class="icon-b" d="M12 34 L32 34 L32 64 L28 64 L28 92 L16 92 L16 64 L12 64 Z"/><circle class="icon-b" cx="78" cy="22" r="8"/><path class="icon-b" d="M68 34 L88 34 L88 64 L84 64 L84 92 L72 92 L72 64 L68 64 Z"/></svg>
  <div class="cell-text">Be extraordinary</div>
</div>

<div class="abs brand" style="top:4355px;height:105px"><span class="brand-name">Quorival</span></div>

</body>
</html>
```